Real Estate Open House & For Sale Signage

I am designing brand new signs for my real estate company. All I have so far are my logo and a business card design. I would like to have designed two different signs, 1. Open House directional sign, 2. For Sale Company sign. Both signs need to will be eye catching from the street, easy to read, identifiable and memorable.

Target Market(s)

Males & females, Ages between 30-65, affluent, educated, professionals.

Industry/Entity Type

Real Estate

Font styles to use
Serif
Sans Serif

Colors
33b8a4
34a7d8
acd137
3277b5

Requirements
Must have
• Must have my company logo & real estate license number visible on the sign. Must be easily visible and eye catching from a moving vehicle. Must have a professional and trustworthy appeal. Must bring to mind real estate.
Nice to have
• Image or icon that will denote real estate and be known as a part of my company identity and marketing theme.
Should not have
• Attached is a feeble attempt at creating my For Sale sign. The information on the sign is accurate, but the design is not appealing to me at all. It feels very amateurish.

```html
<!DOCTYPE html>
<html lang="en">
<head>
<meta charset="utf-8">
<title>For Sale Sign – Kailani Property Advisors</title>
<link rel="stylesheet" href="https://fonts.googleapis.com/css2?family=Anton&family=Open+Sans:wght@600;700;800&display=swap">
<style>
  :root {
    --brand-blue: #3277b5;
    --sky-blue: #34a7d8;
    --lime: #acd137;
    --teal: #33b8a4;
    --leaf: #6fa53a;
    --ink: #2b2b2b;
    --paper: #f4f4f4;
    --white: #ffffff;
  }
  * { box-sizing: border-box; margin: 0; padding: 0; }
  html, body { width: 1200px; height: 850px; overflow: hidden; }
  body { font-family: "Open Sans", Arial, sans-serif; background: var(--paper); }

  .sign {
    position: relative;
    width: 1200px;
    height: 850px;
    overflow: hidden;
    background: linear-gradient(135deg, #ffffff 0%, #f1f1f1 55%, #e9e9e9 100%);
  }

  .brand {
    position: absolute;
    left: 78px;
    top: 185px;
    display: flex;
    align-items: center;
    gap: 18px;
  }
  .brand-dot {
    width: 34px;
    height: 34px;
    border-radius: 50%;
    background: var(--lime);
    flex: none;
  }
  .brand-name {
    font-weight: 700;
    font-size: 46px;
    line-height: 1.15;
    color: var(--lime);
    width: 470px;
  }

  .license-tag {
    position: absolute;
    right: 0;
    top: 41px;
    width: 506px;
    height: 91px;
  }
  .license-tag svg { position: absolute; inset: 0; }
  .license-number {
    position: absolute;
    right: 63px;
    top: 0;
    height: 91px;
    line-height: 91px;
    font-weight: 800;
    font-size: 60px;
    color: var(--white);
    letter-spacing: 1px;
  }

  .headline {
    position: absolute;
    left: 72px;
    top: 324px;
    font-family: "Anton", Impact, sans-serif;
    font-weight: 400;
    font-size: 160px;
    line-height: 1;
    letter-spacing: 2px;
    background: linear-gradient(180deg, var(--sky-blue) 0%, var(--brand-blue) 100%);
    -webkit-background-clip: text;
    background-clip: text;
    color: transparent;
    filter: drop-shadow(-5px 5px 0 var(--ink));
  }

  .tagline {
    position: absolute;
    left: 79px;
    top: 506px;
    font-weight: 800;
    line-height: 1.05;
  }
  .tagline-lead { display: block; font-size: 53px; letter-spacing: -0.5px; color: var(--ink); }
  .tagline-focus { display: block; font-size: 72px; margin-top: -6px; color: var(--leaf); }

  .keys-photo {
    position: absolute;
    left: 712px;
    top: 165px;
    width: 460px;
    height: 370px;
    border-radius: 40px;
    background: radial-gradient(ellipse at 45% 50%, #cfd2d4 0%, #b9bdc0 40%, rgba(238,238,238,0) 75%);
  }

  .waves { position: absolute; left: 0; top: 0; }

  .contact {
    position: absolute;
    right: 90px;
    top: 673px;
    text-align: right;
    color: var(--white);
    font-weight: 700;
  }
  .agent-name { font-size: 66px; line-height: 1.1; }
  .agent-phone { font-size: 87px; line-height: 1.05; margin-top: -11px; }
</style>
</head>
<body>
  <main class="sign">
    <div class="brand">
      <span class="brand-dot"></span>
      <span class="brand-name">Kailani Property Advisors LLC</span>
    </div>

    <div class="license-tag">
      <svg width="506" height="91" viewBox="0 0 506 91" aria-hidden="true">
        <polygon points="46,0 506,0 506,91 0,91" fill="var(--teal)"/>
        <polygon points="72,0 506,0 506,83 14,83" fill="var(--brand-blue)"/>
      </svg>
      <span class="license-number">RB - 40215</span>
    </div>

    <div class="keys-photo" role="img" aria-label="Photo of silver house keys on a ring with a house-shaped keychain"></div>

    <h1 class="headline">FOR SALE</h1>

    <p class="tagline">
      <span class="tagline-lead">YOUR NEIGHBORHOOD</span>
      <span class="tagline-focus">SPECIALIST</span>
    </p>

    <svg class="waves" width="1200" height="850" viewBox="0 0 1200 850" aria-hidden="true">
      <path d="M0,628 C220,760 430,770 640,680 C840,595 1000,560 1200,600 L1200,850 L0,850 Z" fill="var(--lime)"/>
      <path d="M0,652 C230,785 440,790 650,705 C850,622 1010,595 1200,630 L1200,850 L0,850 Z" fill="var(--white)"/>
      <path d="M0,680 C240,810 450,810 660,730 C860,650 1020,625 1200,655 L1200,850 L0,850 Z" fill="var(--brand-blue)"/>
      <g class="phone-badge">
        <circle cx="837" cy="614" r="38" fill="var(--white)"/>
        <circle cx="837" cy="614" r="32" fill="var(--teal)"/>
        <path d="M824,598 l7,-3 l6,11 l-5,4 c3,7 7,11 13,14 l4,-5 l11,6 l-3,7 c-2,3 -6,4 -10,3 c-14,-5 -23,-14 -27,-27 c-1,-4 1,-8 4,-10 z" fill="var(--white)"/>
      </g>
    </svg>

    <div class="contact">
      <p class="agent-name">Lena Hart</p>
      <p class="agent-phone">(808) 555-0142</p>
    </div>
  </main>
</body>
</html>
```